Info-Flyer-Design für Inserate eines Katalogs von Papeterie- und Bürobedarf
Zielgruppe
KOLBA ist ein Schweizer Grosshandelsunternehmen für Papeterie- und Bürobedarf. Kunden sind ausschliesslich professionelle Wiederverkäufer. Endverbraucher werden nicht direkt, sondern über KOLBA Kunden beliefert.
Das Sortiment umfasst neben Papeterie- und Schulartikeln eine kompetente Auswahl im Bereich Bürobedarf. Die Produktepalette wird laufend weiterentwickelt und umfasst auch den Bereich Catering & Kaffee, Hygiene & Reinigung sowie Betriebssicherheit – alles was im modernen Büro benötigt wird.
KOLBA bietet seinen Kunden umfassende Dienstleistungen an. Diese ermöglichen es, das vom Markt geforderte breite und tiefe Sortiment zielgruppengerecht erfolgreich zu vermarkten und effizient zu verteilen. In enger Zusammenarbeit mit unseren Kunden und Lieferanten entwickeln wir unsere Dienstleistungen stetig weiter. Neben den Vermarktungszielen stehen Effizienzziele, die Doppelspurigkeiten in der Wertschöpfungskette vermeiden, im Vordergrund.
Das oberste Ziel von KOLBA ist es, ein zuverlässiger Partner zu sein. Deshalb geniessen Servicegrad und Lieferqualität höchste Priorität. Wir streben nach kooperativen und langfristigen Geschäftsbeziehungen und setzen neue Technologien zum gemeinsamen Nutzen ein.
Aufgabenstellung
In diesem Auftrag geht es darum, dass wir unseren Lieferanten ein Info Flyer zu senden, damit Sie Inserate in unserem nächsten Katalog für das Jahr 21/22 buchen. Es soll lebendig und erfrischend daher kommen. Das Format soll in A4 erstellt sein. Ich benötige am Ende die Original INDD Dokumente. Der Text kann gem. PDF Vorlage vom letzten Jahr übernommen werden, diesen werden wir selbstständig anpassen. Bitte das Logo in der Anlage verwenden sowie das Titelbild . Schrift haben wir ClanOT. Die Titelbalken (grün) haben wir immer so verwendet, da diese auch im Katalog erscheinen, hier kann aber auch die Farbe geändert werden.

```html
<!DOCTYPE html>
<html lang="de">
<head>
<meta charset="utf-8">
<title>KOLBA Office 20/21 – Info-Flyer</title>
<link href="https://fonts.googleapis.com/css2?family=Barlow+Semi+Condensed:wght@300;400;600;700&display=swap" rel="stylesheet">
<style>
  :root {
    --stage: #aaaaaa;
    --paper: #ffffff;
    --brand-yellow: #fdcd34;
    --tagline-yellow: #f5c12e;
    --cream: #fdf7e4;
    --ink: #2f2f2f;
    --ink-soft: #3c3c3c;
    --mock-grey: #ececec;
    --mock-line: #8a8a8a;
    --concrete: #8f9092;
    --concrete-light: #b4b5b6;
    --desk-light: #e3e3e3;
    --desk-yellow: #f7d95c;
  }
  * { margin: 0; padding: 0; box-sizing: border-box; }
  html, body { width: 1200px; height: 848px; overflow: hidden; }
  body {
    background: var(--stage);
    font-family: "Barlow Semi Condensed", "Arial Narrow", sans-serif;
    color: var(--ink);
    position: relative;
  }
  .page {
    position: absolute;
    top: 20px;
    width: 570px;
    height: 803px;
    background: var(--paper);
  }
  .page--cover { left: 22px; }
  .page--info { left: 608px; }

  /* Cover */
  .cover-band {
    position: absolute;
    left: 29px; top: 29px;
    width: 511px; height: 166px;
    background: var(--brand-yellow);
    overflow: hidden;
  }
  .brand-name {
    position: absolute;
    color: var(--paper);
    font-weight: 700;
    letter-spacing: 1px;
    line-height: 1;
  }
  .cover-band .brand-name { right: 30px; top: 10px; font-size: 34px; }
  .cover-title {
    position: absolute;
    left: 10px; top: 8px;
    font-size: 142px;
    font-weight: 600;
    color: var(--paper);
    line-height: 1;
    letter-spacing: -2px;
  }
  .cover-year {
    position: absolute;
    left: 344px; top: 101px;
    font-size: 40px;
    font-weight: 600;
    color: var(--paper);
    line-height: 1;
  }
  .cover-photo {
    position: absolute;
    left: 29px; top: 195px;
    width: 511px; height: 552px;
    background:
      linear-gradient(152deg, transparent 0 52%, rgba(247,217,92,0.85) 52% 100%),
      linear-gradient(180deg,
        var(--concrete) 0%, var(--concrete-light) 22%,
        var(--desk-light) 23%, var(--desk-light) 76%,
        var(--concrete-light) 77%, var(--concrete) 100%);
  }
  .cover-tagline {
    position: absolute;
    right: 43px; top: 756px;
    font-size: 16px;
    font-weight: 600;
    color: var(--tagline-yellow);
  }

  /* Info page */
  .info-band {
    position: absolute;
    left: 29px; top: 30px;
    width: 511px; height: 53px;
    background: var(--brand-yellow);
  }
  .info-band__title {
    position: absolute;
    left: 14px; top: 16px;
    font-size: 16px;
    font-weight: 600;
    color: var(--paper);
    word-spacing: 2px;
  }
  .info-band .brand-name { right: 30px; top: 9px; font-size: 28px; }

  .letter {
    position: absolute;
    left: 43px; top: 115px;
    width: 490px;
    font-size: 11.6px;
    line-height: 17.1px;
    font-weight: 300;
    color: var(--ink-soft);
  }
  .letter__salutation { font-weight: 600; color: var(--ink); }

  .overview {
    position: absolute;
    left: 30px; top: 302px;
    width: 511px; height: 471px;
    background: var(--cream);
  }
  .overview__heading {
    position: absolute;
    left: 13px; top: 15px;
    font-size: 11.8px;
    font-weight: 700;
    letter-spacing: 0.2px;
  }
  .feature-list {
    position: absolute;
    top: 47px;
    list-style: none;
    font-size: 10.4px;
    line-height: 15.2px;
    font-weight: 300;
    color: var(--ink-soft);
  }
  .feature-list--left { left: 13px; width: 240px; }
  .feature-list--right { left: 261px; width: 210px; }
  .feature-list li { position: relative; padding-left: 17px; }
  .feature-list li::before {
    content: "•";
    position: absolute; left: 0; top: 0;
    font-size: 8px;
  }

  .spread-mock {
    position: absolute;
    left: 67px; top: 157px;
    width: 394px; height: 273px;
    background: var(--mock-grey);
  }
  .spread-mock__fold {
    position: absolute;
    left: 193px; top: 6px;
    width: 1px; height: 260px;
    background: var(--mock-line);
  }

  .callout {
    position: absolute;
    font-size: 7.6px;
    line-height: 9.5px;
    font-weight: 700;
    color: #111;
  }
  .callout--swiss { left: 255px; top: 125px; width: 120px; text-align: center; }
  .callout--layout { left: 4px; top: 227px; width: 64px; }
  .callout--tabs { left: 445px; top: 278px; width: 60px; text-align: right; }
  .callout--optics { left: 3px; top: 385px; width: 58px; }
  .callout--sales { left: 153px; top: 441px; width: 120px; text-align: center; }

  .callout-arrows {
    position: absolute;
    left: 0; top: 0;
    width: 511px; height: 471px;
    pointer-events: none;
  }
</style>
</head>
<body>

  <section class="page page--cover">
    <header class="cover-band">
      <span class="brand-name">KOLBA</span>
      <h1 class="cover-title">Office</h1>
      <span class="cover-year">20/21</span>
    </header>
    <div class="cover-photo" role="img" aria-label="Titelbild: Blick von oben auf einen hellgrauen und gelben Bürotisch mit Laptops, Notizblöcken, Tablet, Pflanze und Kaffee, umgeben von bunten Stühlen auf Betonboden"></div>
    <p class="cover-tagline">Ein Gesamtpaket, das Erfolg verspricht.</p>
  </section>

  <section class="page page--info">
    <header class="info-band">
      <h2 class="info-band__title">Office 20/21&nbsp; Sortiment</h2>
      <span class="brand-name">KOLBA</span>
    </header>

    <div class="letter">
      <p class="letter__salutation">Geschätzte Partner,</p>
      <p>die Attraktivität und die Nachfrage bestätigt unser Konzept zur Beibehaltung unseres bewährten Office Kataloges in Druckversion. Als nach wie vor beliebtes Werbemittel besticht auch die neue Ausgabe mit einem neu überarbeiteten, modernen und ansprechenden Layout, einer umfassenden Auswahl an Artikeln und natürlich dem gewohnten, fachkundigen Inhalt. Lassen Sie sich von unserem Office 19/20 überraschen.</p>
      <p>Wir streben eine Auflage von 75‘000 Exemplaren an. Mehr als 250 Fachhändler werden diesen Katalog schweizweit in drei Sprachen zum Einsatz bringen. Der Umfang beträgt wiederum ca. 580 Seiten, die Laufzeit beträgt zwei Jahre. Der Office 19/20 wird ab Mitte Dezember 2018 an unsere Fachhändler ausgeliefert.</p>
    </div>

    <div class="overview">
      <h3 class="overview__heading">VERSTÄNDLICHE KATALOGÜBERSICHT</h3>
      <ul class="feature-list feature-list--left">
        <li>Umfangreich und kompetent auf ca. 580 Seiten</li>
        <li>Verkaufsfördernde Anwendungsbilder</li>
        <li>Optimierte und übersichtliche Seitengestaltung</li>
        <li>Zusätzliche Informationen zu Artikelnutzen oder Anwendung</li>
      </ul>
      <ul class="feature-list feature-list--right">
        <li>Piktogramme zur schnelleren Orientierung</li>
        <li>Kaffee, Getränke, Snacks und neue Zusatzsortimente für das Liefergeschäft</li>
      </ul>

      <div class="spread-mock">
        <div class="spread-mock__fold"></div>
      </div>

      <p class="callout callout--swiss">Hinweis auf Schweizer<br>Qualitätsprodukte</p>
      <p class="callout callout--layout">Fixe Platzzutei-<br>lung für<br>Logos, Bilder und<br>Piktogramme</p>
      <p class="callout callout--tabs">Tabs zur<br>schnelleren<br>Auffindung<br>der<br>Rubriken</p>
      <p class="callout callout--optics">Piktogramme<br>zur Verbesse-<br>rung der<br>Optik und der<br>Verbindlichkeit</p>
      <p class="callout callout--sales">Piktogramme<br>Verkaufsfördernde<br>Anwendungsbilder</p>

      <svg class="callout-arrows" viewBox="0 0 511 471" aria-hidden="true" fill="none" stroke="#111" stroke-width="1.3" stroke-linecap="round" stroke-linejoin="round">
        <path d="M302 148 C306 168 298 184 284 193"/>
        <path d="M284 184 L284 193 L293 191"/>
        <path d="M38 269 C34 287 44 302 62 309"/>
        <path d="M53 310 L62 309 L57 302"/>
        <path d="M453 304 L415 313"/>
        <path d="M422 307 L415 313 L423 317"/>
        <path d="M51 402 L83 423"/>
        <path d="M74 422 L83 423 L79 415"/>
        <path d="M268 462 C285 458 296 444 297 425"/>
        <path d="M292 432 L297 425 L301 433"/>
      </svg>
    </div>
  </section>

</body>
</html>
```